Business Card design for Founder and CEO of new shoe company

I am looking for a business card design for my new shoe company called Strapwell.

I am launching the company this April. Strapwell shoes offers slip-on athletic and casual style shoes for men and women. The unique selling point of the brand is that all of our shoe exist without shoelaces. I have included a link to the website to offer additional information about the company, see product images, and gain inspiration for the design. You can use the store owner password "Strapwell" to access the website.

www.Strapwell.example

Thanks,
Dan Hollis

Target Market(s)

Active Men and Women ages 16-45

Industry/Entity Type

Business

Contact Information for Business Card

Dan Hollis
Founder and CEO
www.Strapwell.example
danhollis@Strapwell.example
888-555-0187 / 888-5STRAPW
Strapwell, LLC
2284 N Tamsin Ave
Chicago, IL 60699

Requirements
Must have
• Be able to quickly and easily tell that Strapwell is a shoe company from the business card

```html
<!DOCTYPE html>
<html lang="en">
<head>
<meta charset="utf-8">
<title>Strapwell – Business Card</title>
<link rel="stylesheet" href="https://fonts.googleapis.com/css2?family=Open+Sans:wght@400;700&display=swap">
<style>
  :root {
    --page-bg: #e9e6e1;
    --card-bg: #ffffff;
    --strip-black: #0b0b0b;
    --ink: #1a1a1a;
    --accent-magenta: #d3289f;
    --contact-blue: #2061c9;
    --rule: #1a1a1a;
  }
  * { box-sizing: border-box; margin: 0; padding: 0; }
  html, body {
    width: 1200px; height: 800px; overflow: hidden;
    background: var(--page-bg);
    font-family: "Open Sans", Verdana, sans-serif;
  }
  .business-card {
    position: absolute; left: 80px; top: 130px;
    width: 1040px; height: 540px;
    background: var(--card-bg);
    border-radius: 14px;
    box-shadow: 0 6px 18px rgba(0,0,0,0.18);
  }
  .photo-strip {
    position: absolute; top: 38px;
    width: 262px; height: 458px;
    background: var(--strip-black);
    padding: 18px 22px;
    display: flex; flex-direction: column; gap: 14px;
  }
  .photo-strip--left { left: 42px; }
  .photo-strip--right { right: 42px; top: 48px; width: 268px; }
  .product-photo { flex: 1; width: 100%; }
  .shoe-white   { background: linear-gradient(180deg, #f4f4f4 0%, #e2e2e2 55%, #4a4a4a 100%); }
  .shoe-duo     { background: linear-gradient(100deg, #e4e4e4 0%, #cfcfcf 40%, #2bb6dc 60%, #3a3a3a 100%); }
  .shoe-blue    { background: linear-gradient(180deg, #e9e9e9 0%, #2eb9e0 50%, #2a2a2a 100%); }
  .shoe-orange  { background: linear-gradient(180deg, #f2f2f2 0%, #6a6a6a 45%, #e97a2a 60%, #d8d8d8 100%); }
  .shoe-pink    { background: linear-gradient(180deg, #f2f2f2 0%, #3f62c8 45%, #d53ca6 65%, #e6e6e6 100%); }
  .shoe-pair    { background: linear-gradient(100deg, #f2f2f2 0%, #6d6d6d 35%, #e98a3a 45%, #39b6e0 70%, #f2f2f2 100%); }

  .card-details {
    position: absolute; left: 330px; right: 330px; top: 30px;
    text-align: center;
  }
  .brand-name {
    display: flex; align-items: center; justify-content: center; gap: 12px;
    font-size: 38px; font-weight: 400; color: var(--ink);
    letter-spacing: 1px; line-height: 1.2;
  }
  .brand-mark { width: 18px; height: 18px; background: var(--ink); }
  .person-name {
    margin-top: 36px;
    font-size: 30px; font-weight: 700; color: var(--accent-magenta);
    line-height: 1.1;
  }
  .person-title { font-size: 19px; color: var(--ink); line-height: 1.4; }
  .contact-list { margin-top: 30px; list-style: none; }
  .contact-item {
    font-size: 22px; color: var(--contact-blue);
    line-height: 1.3; padding: 4px 0 8px;
  }
  .contact-item--ruled { position: relative; }
  .contact-item--ruled::after {
    content: ""; position: absolute; left: 50%; bottom: 0;
    width: 230px; height: 2px; margin-left: -115px;
    background: var(--rule);
  }
  .contact-item--email::after { width: 230px; }
  .mailing-address {
    font-style: normal; font-size: 22px; color: var(--contact-blue);
    line-height: 1.55; margin-top: 4px;
  }
</style>
</head>
<body>
  <article class="business-card">
    <div class="photo-strip photo-strip--left">
      <div class="product-photo shoe-white" role="img" aria-label="Product photo: white and grey strapless slip-on sneaker"></div>
      <div class="product-photo shoe-duo" role="img" aria-label="Product photo: grey and turquoise slip-on sneakers side by side"></div>
      <div class="product-photo shoe-blue" role="img" aria-label="Product photo: turquoise and black slip-on sneaker"></div>
    </div>

    <div class="card-details">
      <div class="brand-name"><span class="brand-mark"></span>Strapwell</div>
      <h1 class="person-name">Dan Hollis</h1>
      <p class="person-title">Founder and CEO</p>
      <ul class="contact-list">
        <li class="contact-item contact-item--ruled">888-555-0187</li>
        <li class="contact-item contact-item--ruled">www.Strapwell.example</li>
        <li class="contact-item contact-item--ruled contact-item--email">danhollis@Strapwell.example</li>
      </ul>
      <address class="mailing-address">
        Strapwell, LLC<br>
        2284 N Tamsin Ave<br>
        Chicago, IL 60699
      </address>
    </div>

    <div class="photo-strip photo-strip--right">
      <div class="product-photo shoe-orange" role="img" aria-label="Product photo: grey and orange slip-on sneakers"></div>
      <div class="product-photo shoe-pink" role="img" aria-label="Product photo: blue and pink slip-on sneaker"></div>
      <div class="product-photo shoe-pair" role="img" aria-label="Product photo: grey-orange and turquoise slip-on sneakers facing each other"></div>
    </div>
  </article>
</body>
</html>
```